Yoga site design

we need to design a homepage and content sections for our yoga portal

Verandel

Verandel is a yoga community ecosystem dedicated to the yoga enthusiasts and adopters of an active lifestyle based upon yoga and ayurvedic living. The objective of Verandel is to expand the involvment and adoption of yoga across the communities and facilitate the profitable growth of the various stakeholders and service providers involved with the ecosystem

Site descriptor

The site will have 4 building blocks/functionalities as specified below;

1.Directory functionality wherein it would list yoga classes/events/ workshop/ retreats and show calendar by dates and place
1. when
2. where
3. what
4. who
5. cost
6. durations

2.Search functionality

a.Find a yoga class/studio close to you (location tagging/google maps)
search/show by studioname/ teacher/ Private sessions/ yoga family
1. when
2. where
3. what
4. who
5. cost

3.Content publishing capabilty

a.Micro sites studio directory/ teachers/ frequent event holders/ therapists - contributors and serviceproviders
1. words of descriprion about yourself and your business
2. an email address
3. a live web link
4. google maps
5. contact phone number
6. a logo upload
7. a picture of themselves, (we need to specify size)
8 Weekly/monthly calendar - where thay are and when

b.Topical content
• columns written by a refference or celebrity
• parts in Montly newsletter and/or downloadable

c.Monthly Newsletter

d.What is New/News/Flash Happenings on the Site

e.Community Board
a virtual meeting place on a login and username basis
• Twitter
• chat
• yoganetwork - offline community build
• find a group close to you!

4.E-commerce capability (Yoga store)
by category;
• yoga props
• yoga clothes
• Ayurvedic related products
• Books/Music/dvd
• skin/body
tickets to events -
Updates

Reason: not enough iterations

Reason: i was unwell for the last two weeks

Target Market(s)

yoga enthusiasts across multiple cities in europe and americas

Industry/Entity Type

Building

Requirements
Must have
• the design should not be intrusive and allow for multiple city instances to be created using the same deisgn sensibilities
Should not have
• i do not need any tech coding.

```html
<!DOCTYPE html>
<html lang="en">
<head>
<meta charset="utf-8">
<title>Verandel – Yoga Portal</title>
<link href="https://fonts.googleapis.com/css2?family=Arimo:wght@400;700&family=Questrial&display=swap" rel="stylesheet">
<style>
:root{
  --sky-top:#5fc3ea;
  --sky-bottom:#ffffff;
  --page:#ffffff;
  --panel:#f6f6f6;
  --brand-blue:#4aa6f0;
  --nav-top:#63b3f5;
  --nav-bottom:#2e86dc;
  --orange:#f07a12;
  --orange-band-top:#f3a623;
  --orange-band-bottom:#c97c0a;
  --ink:#222222;
  --muted:#555555;
  --grey-text:#6b6b6b;
  --link:#3c9be6;
  --cyan-head:#3fb0de;
  --gold-head:#c99a3c;
  --green-head:#0f9a0f;
  --red-head:#d0281c;
  --hairline:#e2e2e2;
}
*{box-sizing:border-box;margin:0;padding:0}
html,body{width:1200px;height:900px;overflow:hidden}
body{
  font-family:"Arimo",Arial,sans-serif;
  background:linear-gradient(180deg,var(--sky-top) 0,#a9def4 380px,var(--sky-bottom) 620px);
  position:relative;color:var(--ink);
}
.page{
  position:absolute;left:110px;top:6px;width:980px;height:900px;
  background:#d7eefa;border-radius:16px 16px 0 0;padding:9px 10px 0;
}
.page-inner{position:relative;width:960px;height:900px;background:var(--page);border-radius:10px 10px 0 0;overflow:hidden}
/* header */
.brand{position:absolute;left:10px;top:26px;display:flex;align-items:flex-start}
.brand-mark{width:92px;height:92px;border-radius:50%;background:#e9a25a;margin-right:18px}
.brand-name{font-size:48px;font-weight:700;color:var(--brand-blue);letter-spacing:-1px;line-height:1;margin-top:20px}
.tagline{position:absolute;left:126px;top:99px;font-family:"Questrial",sans-serif;font-size:18px;color:var(--grey-text)}
.login{position:absolute;right:10px;top:0;display:flex;align-items:flex-start}
.field{width:122px;height:30px;border:1px solid #d8d8d8;border-radius:5px;background:linear-gradient(#fff,#eee);
  font-size:11px;color:#555;padding:9px 12px;margin:6px 15px 0 0}
.btn-login{width:82px;height:36px;background:linear-gradient(#fafafa,#dedede);color:var(--brand-blue);font-weight:700;font-size:16px;text-align:center;line-height:36px;border-radius:4px 0 0 4px}
.btn-signup{width:78px;height:36px;background:linear-gradient(#2a8bd8,#0f5ea8);color:#fff;font-weight:700;font-size:16px;text-align:center;line-height:36px;border-radius:0 4px 4px 0}
.search{position:absolute;left:490px;top:60px;width:460px;height:58px;border:4px solid #a9d2f5;border-radius:10px;background:linear-gradient(#fff,#eef3f7);padding:0 12px 0 32px;display:flex;align-items:center;justify-content:space-between}
.search span{font-size:13px;font-weight:700;color:#9a9a9a}
.search b{display:block;height:30px;padding:0 15px;line-height:30px;border-radius:7px;background:linear-gradient(#f7f7f7,#d5d5d5);font-size:13px;color:var(--link);border:1px solid #ccc}
/* nav */
.nav{position:absolute;left:0;top:140px;width:960px;height:34px;background:linear-gradient(var(--nav-top),var(--nav-bottom));display:flex;align-items:flex-end}
.nav a{color:#fff;font-weight:700;font-size:16px;text-decoration:none;height:34px;line-height:34px}
.nav .current{background:#fff;color:var(--orange);border-radius:4px 4px 0 0;width:100px;text-align:center;height:29px;line-height:31px;margin-left:10px;margin-right:33px}
.nav a+a{margin-right:0}
/* hero */
.hero{position:absolute;left:10px;top:209px;width:640px;height:358px;border:6px solid #b8b2ae;border-radius:4px;background:radial-gradient(ellipse at 60% 40%,#d8c8b4,#8a7765 55%,#3d342c);overflow:hidden}
.welcome{position:absolute;left:20px;top:0;width:222px;height:210px;background:rgba(40,30,22,.8);border-radius:0 0 4px 4px;padding:10px 14px;color:#fff}
.welcome h2{font-size:18px;font-weight:400;line-height:23px}
.welcome h2 strong{font-weight:700}
.welcome p{font-size:12.5px;line-height:20px;margin-top:24px;color:#eee}
.detail{display:inline-block;margin-top:16px;width:92px;height:32px;background:linear-gradient(#fff,#d8d8d8);border-radius:4px;color:var(--link);font-weight:700;font-size:18px;text-align:center;line-height:32px}
.pager{position:absolute;left:235px;bottom:0;width:160px;height:42px;background:#2b2b2b;border-radius:3px 3px 0 0;display:flex;align-items:center;padding-left:12px;gap:8px}
.pager i{width:13px;height:13px;border-radius:50%;background:#ddd}
.pager i.on{background:#1f7fd0}
/* news */
.news{position:absolute;left:669px;top:209px;width:281px}
.news h3{height:36px;background:linear-gradient(#6cb8f5,#3b93e0);border-radius:4px 4px 0 0;font-size:17px;padding:9px 10px;color:#1c2e3e}
.news-item{display:flex;padding:14px 0 10px 15px;border-bottom:1px solid var(--hairline);height:107px}
.news-thumb{width:86px;height:77px;border:3px solid #fff;box-shadow:0 0 3px #bbb;background:linear-gradient(#f1ebe5,#d9cfc6);flex:none;margin-right:15px}
.news-item p{font-size:12.5px;line-height:20px;color:#333;text-align:justify;margin-top:-4px}
.news-item a{color:var(--link);text-decoration:none;display:block}
/* banner */
.banner{position:absolute;left:10px;top:590px;width:940px;height:56px;background:linear-gradient(var(--orange-band-top),var(--orange-band-bottom));border-radius:4px;text-align:center;line-height:56px;font-size:24px;letter-spacing:-.5px;color:#111}
.banner strong{font-weight:700}
/* cards */
.card{position:absolute;top:678px;width:218px;height:230px;background:var(--panel)}
.card h4{height:35px;color:#fff;font-size:16px;padding:9px 12px;border-radius:3px 3px 0 0}
.card .pic{margin:23px 8px 0;height:100px;border:3px solid #fff;box-shadow:0 0 3px #bbb}
.card h5{font-size:12px;color:var(--link);margin:16px 0 0 10px}
.card p{font-size:12.5px;color:#333;margin:6px 0 0 10px}
.c1{left:10px}.c1 h4{background:var(--cyan-head)}.c1 .pic{background:linear-gradient(#d4c6a4,#8e8a76 60%,#9b7cbc)}
.c2{left:252px}.c2 h4{background:var(--gold-head)}.c2 .pic{background:linear-gradient(#e6e6e6,#9a9a9a)}
.c3{left:490px}.c3 h4{background:var(--green-head)}.c3 .pic{background:radial-gradient(circle,#d1403a 0,#e9e9e9 45%,#fff 70%)}
.c4{left:731px}.c4 h4{background:var(--red-head)}.c4 .pic{background:radial-gradient(circle,#c2171c 0,#c91d20 35%,#fff 60%)}
</style>
</head>
<body>
<div class="page"><div class="page-inner">
  <header>
    <div class="brand"><div class="brand-mark"></div><div class="brand-name">Verandel</div></div>
    <div class="tagline">active lifestyle and ayurvedic living community</div>
    <div class="login">
      <div class="field">Username</div><div class="field">Password</div>
      <div class="btn-login">Login</div><div class="btn-signup">Sign Up</div>
    </div>
    <div class="search"><span>enter keyword</span><b>Search yoga portal</b></div>
  </header>
  <nav class="nav">
    <a class="current">Home</a>
    <a style="margin-right:40px">Yoga tips</a>
    <a style="margin-right:26px">Yoga Course</a>
    <a style="margin-right:31px">Online Shop</a>
    <a style="margin-right:35px">Community</a>
    <a style="margin-right:48px">Multimedia</a>
    <a style="margin-right:48px">Support</a>
    <a>Contact Us</a>
  </nav>
  <section class="hero" role="img" aria-label="Photo of a woman in a seated forward-bend yoga pose">
    <div class="welcome">
      <h2>Welcome to<br><strong>Verandel</strong></h2>
      <p>Lorem ipsum dolor sit amet, consectetur adipiscing elit. Duis sit amet dolor arcu.</p>
      <span class="detail">Detail</span>
    </div>
    <div class="pager"><i class="on"></i><i></i><i></i><i></i><i></i>
      <svg width="34" height="16" viewBox="0 0 34 16"><path d="M10 2 4 8l6 6M22 2l6 6-6 6" fill="none" stroke="#f07a12" stroke-width="3"/></svg>
    </div>
  </section>
  <aside class="news">
    <h3>News and Events</h3>
    <div class="news-item"><div class="news-thumb" role="img" aria-label="Photo of a woman meditating"></div><p>Lorem ipsum dolor sit amet, consectetur adipiscing elit. Duis sit amet.<a>More stories &gt;&gt;</a></p></div>
    <div class="news-item"><div class="news-thumb" role="img" aria-label="Photo of a woman meditating"></div><p>Lorem ipsum dolor sit amet, consectetur adipiscing elit. Duis sit amet.<a>More stories &gt;&gt;</a></p></div>
    <div class="news-item"><div class="news-thumb" role="img" aria-label="Photo of a woman meditating"></div><p>Lorem ipsum dolor sit amet, consectetur adipiscing elit. Duis sit amet.<a>More stories &gt;&gt;</a></p></div>
  </aside>
  <div class="banner">TEACHER TRAINING WEEK - AUG 20 - 31 2016. <strong>BOOK ONLINE NOW!</strong></div>
  <article class="card c1"><h4>TRAINING WEEK</h4><div class="pic" role="img" aria-label="Photo of a yoga class in a studio"></div><h5>COURSE TITLE</h5><p>Lorem ipsum dolor sit amet, con-</p></article>
  <article class="card c2"><h4>FEATURED WORKSHOP</h4><div class="pic" role="img" aria-label="Photo of two people in a partner yoga pose"></div><h5>WORKSHOP TITLE</h5><p>Lorem ipsum dolor sit amet, con-</p></article>
  <article class="card c3"><h4>PUBLISHER TIPS</h4><div class="pic" role="img" aria-label="Image of a yoga tips book cover"></div><h5>LOREM &nbsp;TITLE</h5><p>Lorem ipsum dolor sit amet, con-</p></article>
  <article class="card c4"><h4>WHAT’s NEW IN SHOP</h4><div class="pic" role="img" aria-label="Photo of a red yoga top"></div><h5>PRODUCT NAME &nbsp;TITLE</h5><p>Lorem ipsum dolor sit amet, con-</p></article>
</div></div>
</body>
</html>
```